Desktop and Networking Support Course 9.17.25

Important the ad should not be very busy with the text taking up the major part of the ad .. please do not make the text so big that it takes up most of the ad..
Flyer Design Brief for Graphic Artist
also i am looking for something unique or creative that it will stand out .
Size & Layout:
Full Page with Bleed: 8” x 10.75” + 0.25” bleed on all sides.
Footer Space: Leave a 1-inch margin at the bottom for footer content (e.g., contact info, logo, or call-to-action).
Target Audience:
College-age students (around 24 years old)
Located in the USA
Interested in creative, professional, and career-building opportunities
Purpose:
To attract students to enroll in a college program
Flyer should be eye-catching, unique, and creative
Text must be clear and readable,
Design Style:
Use vector art, typography, or photography — your choice
If using photography, feature a white young professional USA citizen:
Wearing a white collared shirt
not with long hair
Creative Direction:
The flyer should stand out visually — something people would want to look at and keep
Showcase creativity and professionalism
Use bold colors, dynamic layout, or unexpected design elements to grab attention
Avoid clutter — keep the design balanced and clean
Text Suggestions (can be adjusted):
Footer,
please leave one inch on the bottom for the footer

```html
<!DOCTYPE html>
<html lang="en">
<head>
<meta charset="utf-8">
<title>Desktop &amp; Network Support Course Flyer</title>
<link rel="stylesheet" href="https://fonts.googleapis.com/css2?family=Source+Sans+3:ital,wght@0,400;0,600;0,700;0,900;1,400&display=swap">
<style>
  :root {
    --blue-base: #1a5a8e;
    --blue-deep: #134a80;
    --blue-stripe: #2b7fbb;
    --blue-glow: #3aa2da;
    --blue-pill: #1c5990;
    --white: #ffffff;
    --shirt-light: #eceff2;
    --shirt-shade: #c9d0d8;
    --ink-blue: #1d5a8e;
    --shadow: rgba(8, 30, 60, 0.55);
  }
  * { margin: 0; padding: 0; box-sizing: border-box; }
  html, body { width: 822px; height: 1200px; overflow: hidden; background: #dcdcdc; }
  .flyer {
    position: relative;
    width: 822px;
    height: 1200px;
    font-family: "Source Sans 3", "Source Sans Pro", sans-serif;
    color: var(--white);
    overflow: hidden;
  }
  .hero {
    position: absolute;
    inset: 0 0 133px 0;
    background: var(--blue-base);
    overflow: hidden;
  }
  .hero-shapes { position: absolute; inset: 0; }
  .headline-band {
    position: absolute;
    left: 0; top: 68px;
    width: 505px; height: 172px;
    background: var(--blue-deep);
  }
  .headline {
    position: absolute;
    left: 57px; top: 80px;
    font-weight: 700;
    line-height: 1;
    text-shadow: 3px 3px 0 var(--shadow);
  }
  .headline .line-one { display: block; font-size: 86px; letter-spacing: 0.5px; }
  .headline .line-two { display: block; font-size: 63px; margin-top: 2px; letter-spacing: -0.5px; }
  .course-title {
    position: absolute;
    left: 55px; top: 268px;
    font-size: 31px;
    font-weight: 600;
    line-height: 38px;
    text-shadow: 2px 2px 0 var(--shadow);
  }
  .portrait {
    position: absolute;
    left: 322px; top: 362px;
    width: 500px; height: 705px;
    border-radius: 200px 200px 0 0;
    background: linear-gradient(180deg, #2c3a48 0%, #c79c85 28%, var(--shirt-light) 55%, var(--shirt-shade) 100%);
    opacity: 0.9;
  }
  .features {
    position: absolute;
    left: 65px; top: 349px;
    list-style: none;
    font-size: 24px;
    font-weight: 600;
    line-height: 32px;
    text-shadow: 2px 2px 0 var(--shadow);
  }
  .features li { margin-bottom: 29px; }
  .features li .indent { display: block; padding-left: 4px; }
  .features li.ranked { margin-bottom: 30px; }
  .features .source {
    display: block;
    padding-left: 8px;
    font-size: 14px;
    font-weight: 400;
    font-style: italic;
    line-height: 18px;
    text-shadow: none;
  }
  .pill {
    position: absolute;
    height: 45px;
    border-radius: 23px;
    background: var(--blue-pill);
    border: 2px solid var(--white);
    border-top-color: transparent;
    border-left-color: rgba(255,255,255,0.5);
    font-size: 26px;
    font-weight: 700;
    text-align: center;
    line-height: 41px;
  }
  .pill-format { left: 138px; top: 927px; width: 428px; }
  .pill-scholarship { left: 253px; top: 985px; width: 428px; }
  .footer {
    position: absolute;
    left: 0; bottom: 0;
    width: 822px; height: 133px;
    background: var(--white);
    color: var(--ink-blue);
  }
  .brand-mark {
    position: absolute;
    left: 72px; top: 20px;
    width: 72px; height: 72px;
    border-radius: 50%;
    background: var(--ink-blue);
    color: var(--white);
    font-size: 11px;
    font-weight: 700;
    line-height: 13px;
    display: flex; align-items: center; justify-content: center;
    text-align: center;
  }
  .contact {
    position: absolute;
    left: 168px; top: 25px;
    font-size: 16px;
    font-weight: 600;
    font-style: normal;
    line-height: 21px;
  }
</style>
</head>
<body>
<main class="flyer">
  <section class="hero">
    <svg class="hero-shapes" width="822" height="1067" viewBox="0 0 822 1067" aria-hidden="true">
      <polygon points="0,900 822,110 822,240 0,1030" fill="var(--blue-stripe)"/>
      <polygon points="29,1067 822,300 822,560 180,1067" fill="var(--blue-stripe)"/>
      <circle cx="247" cy="640" r="118" fill="var(--blue-glow)" opacity="0.55"/>
      <polyline points="633,106 738,106 738,575" fill="none" stroke="var(--white)" stroke-width="1.5"/>
    </svg>
    <div class="headline-band"></div>
    <h1 class="headline">
      <span class="line-one">YOUR CAREER</span>
      <span class="line-two">IS JUST A CLICK AWAY</span>
    </h1>
    <h2 class="course-title">• Desktop &amp; Network Support Course</h2>
    <div class="portrait" role="img" aria-label="Photo of a young professional with short dark hair in a white collared shirt"></div>
    <ul class="features">
      <li>Master Modern<span class="indent">Operating Systems</span></li>
      <li>%90 Employment Rate<span class="indent">– Class of 2024</span></li>
      <li class="ranked">Prepare for 3 of the<span class="indent">Top 10 Tech Jobs</span><span class="source">Tech Careers Review 2025</span></li>
      <li>Hands-On Desktop<span class="indent">&amp; Network Training</span></li>
      <li>Real-World<span class="indent">Troubleshooting Skills</span></li>
      <li>Ready for IT Jobs</li>
    </ul>
    <div class="pill pill-format">In-Person and Remote Options</div>
    <div class="pill pill-scholarship">Partial Scholarships Offered</div>
  </section>
  <footer class="footer">
    <div class="brand-mark">Northbridge<br>Tech</div>
    <address class="contact">
      48 Harbor Lane, Brookfield, NY 10087<br>
      Phone: (555) 010-2468 | Email: info@northbridgetech.edu<br>
      Follow us: @northbridgetech
    </address>
  </footer>
</main>
</body>
</html>
```